Profesional personal website needs design and business card

I need a business card with my professional name as a logo "Orlan Vitality" for my business. I am a Wellness Coach, consultant and trainer. So it should be professional, wellness oriented and modern.

Target Market(s)

Private clients, governments, corporations. Luxury and high market.

Industry/Entity Type

Health And Wellness

Contact Information for Business Card

Orlan Vitality should be the logo

Colors

Designer to choose colors to be used in the design.

Requirements
Must have
• Orlan Vitality
• Name: Dario Montalbe
• Wellness Coach, Consultant & Trainer.
• Website: www.orlanvitality-example.com
• Phone:
• Spain (+34) 612 480 597
• (USA) +1 (555) 318 0264
Nice to have
• The most important is the design of "Orlan Vitality", as this is going to be my personal brand logo. It should be professional, wellness, high end and actual.
Should not have
• no golds, no baroque style..

```html
<!DOCTYPE html>
<html lang="en">
<head>
<meta charset="utf-8">
<title>Orlan Vitality — Business Card</title>
<link rel="stylesheet" href="https://fonts.googleapis.com/css2?family=Montserrat:wght@400;500;700&display=swap">
<style>
  :root {
    --backdrop: #161616;
    --card: #2a2a2a;
    --card-edge: #232323;
    --accent: #f5c000;
    --ink: #ffffff;
    --muted: #e8e8e8;
  }
  * { box-sizing: border-box; margin: 0; padding: 0; }
  html, body {
    width: 1200px; height: 900px; overflow: hidden;
    background: radial-gradient(ellipse at 55% 40%, #2c2c2c 0%, var(--backdrop) 70%);
    font-family: "Montserrat", sans-serif;
  }
  .sheet { position: relative; width: 1200px; height: 900px; }
  .card {
    position: absolute; left: 260px; width: 680px; height: 388px;
    background: linear-gradient(135deg, var(--card-edge) 0%, var(--card) 55%, #333 100%);
    border-bottom: 7px solid var(--accent);
    box-shadow: 0 18px 40px rgba(0,0,0,.55);
  }
  .card--front { top: 44px; }
  .card--back { top: 468px; }

  .brand-name {
    font-family: "Montserrat", sans-serif;
    font-weight: 500; color: var(--ink);
    letter-spacing: 1px; line-height: 1.1;
    white-space: nowrap;
  }
  .card--front .brand-name {
    position: absolute; left: 0; right: 0; top: 160px;
    text-align: center; font-size: 40px;
  }
  .card--back .brand-name {
    position: absolute; right: 40px; top: 44px;
    text-align: right; font-size: 34px;
  }

  .holder { position: absolute; left: 50px; top: 150px; }
  .holder__name {
    font-weight: 700; font-size: 26px; letter-spacing: 1px;
    text-transform: uppercase; color: var(--accent);
  }
  .holder__role {
    margin-top: 4px; font-size: 17px; line-height: 1.3; color: var(--muted);
  }

  .rule {
    position: absolute; left: 50px; right: 40px; top: 262px;
    height: 2px; background: var(--accent);
  }

  .contact {
    position: absolute; left: 50px; top: 282px;
    font-size: 15.5px; line-height: 1.7; color: var(--ink);
  }
  .contact .label, .contact .sep, .contact .hl { color: var(--accent); }
  .contact .sep { margin: 0 6px; }
</style>
</head>
<body>
<main class="sheet">
  <section class="card card--front" aria-label="Card front">
    <div class="brand-name">Orlan Vitality</div>
  </section>

  <section class="card card--back" aria-label="Card back">
    <div class="brand-name">Orlan Vitality</div>

    <div class="holder">
      <h1 class="holder__name">Dario Montalbe</h1>
      <p class="holder__role">Wellness Coach,<br>Consultant &amp; Trainer</p>
    </div>

    <div class="rule"></div>

    <div class="contact">
      <p><span class="label">P:</span> (+34) 612 480 597(Spain)<span class="sep">|</span><span class="label">P:</span> +1 (555) 318 0264(USA)</p>
      <p><span class="label">E:</span> info@orlanvitality-example.com<span class="sep">|</span><span class="label">W:</span> www.<span class="hl">orlanvitality-example</span>.com</p>
    </div>
  </section>
</main>
</body>
</html>
```